Business Cards for our company

Hi there,

we have successfully designed a logo with ArtHive and would like now to design our business cards. We would like to keep the colours and the look-and-feel of the logo. Please send in variations with two or three colours and one or two sides. I promise to respond to every single submission.

Many thanks and happy new year.

All the best,
Gustav

Target Market(s)

B2B

Industry/Entity Type

Trade

Contact Information for Business Card

We have successfully designed a logo with ArtHive and would like now to design our business cards. We would like to keep the colours and the look-and-feel of the logo. Please send in variations with two or three colours and one or two sides. I promise to respond to every single submission.

Font styles to use
Serif
Sans Serif
Script

Requirements
Must have
• These information should be on the business card, grouped as you suggest, and we think using small pictograms for mobile, email, etc is pretty helpful:
• Gustav Ortlieb (first and second name)
• Geschäftsführer/ Managing Director (title)
• KtK Warenkontor GmbH (company name and legal form)
• Hasenbergsteige 31/2 (street and house number)
• 70899 Talhausen (zip code and town)
• +491609381746 (mobile)
• +4971419273065 (work)
• g.ortlieb@ktk-warenkontor.example (email)
• www.ktk-warenkontor.example (web)
Nice to have
• Spectacular and interesting layout and design. You look at it and think, wow, that's not the normal stuff.
• We think of ourselves as bridge-builders between businesses (international producers on the one hand, and retail chains on the other hand) and we translate, organise and manage projects where both partners are involved, but it's difficult for them to cooperate due to language barriers and different working cultures.
• This is why we have the n between the B's shaped as a bridge, and the green arc supports this idea. Maybe you could play with this idea...
Should not have
• the standard layout that everybody has

```html
<!DOCTYPE html>
<html lang="de">
<head>
<meta charset="utf-8">
<title>KtK Warenkontor – Visitenkarte</title>
<link href="https://fonts.googleapis.com/css2?family=Ubuntu:wght@500;700&family=Nunito:wght@400&display=swap" rel="stylesheet">
<style>
  :root{
    --stage:#a8a8a8;
    --label:#333333;
    --card-dark:#38383a;
    --mark-box:#555556;
    --mark-frame:#e2e2e2;
    --mark-ink:#161616;
    --brand-green:#3cb043;
    --rule-green:#2f9e6e;
    --info-top:#cfe8ca;
    --info-bottom:#6cc466;
    --ink:#1c1c1c;
  }
  *{margin:0;padding:0;box-sizing:border-box}
  html,body{width:1200px;height:1200px;overflow:hidden;background:var(--stage)}
  .canvas{position:relative;width:1200px;height:1200px}
  .side-label{position:absolute;top:124px;width:540px;text-align:center;
    font:700 56px/1 "Ubuntu",sans-serif;color:var(--label)}
  .side-label--back{left:30px}
  .side-label--front{left:626px}
  .card{position:absolute;top:190px;width:540px;height:900px;overflow:hidden;
    background:var(--card-dark)}
  .card--back{left:30px}
  .card--front{left:626px}
  .mark{position:absolute;width:360px;height:150px;background:var(--mark-box);
    border:2px solid var(--mark-frame);display:flex;align-items:center;justify-content:center}
  .mark__name{font:700 36px/1 "Ubuntu",sans-serif;color:var(--mark-ink);letter-spacing:.5px}
  .accent-block{position:absolute;width:81px;height:150px;
    background:linear-gradient(160deg,#3cb043 0%,#9ed89a 55%,#eef8ec 100%)}
  .company{position:absolute;width:360px;text-align:center;
    font:700 24px/1 "Ubuntu",sans-serif;color:var(--brand-green)}
  .rule{position:absolute;left:93px;right:0;top:348px;height:11px;background:var(--rule-green)}
  .info{position:absolute;left:0;top:402px;width:540px;height:498px;
    background:linear-gradient(180deg,var(--info-top) 0%,var(--info-bottom) 100%)}
  .info-row{position:absolute;left:0;width:540px;height:90px}
  .info-row::after{content:"";position:absolute;left:20px;right:0;bottom:0;height:6px;
    background:radial-gradient(ellipse at 50% 0%,rgba(0,0,0,.22),rgba(0,0,0,0) 70%)}
  .icon-box{position:absolute;left:87px;top:12px;width:54px;height:54px;
    border:3px solid var(--ink);display:flex;align-items:center;justify-content:center}
  .info-text{position:absolute;left:168px;top:10px;font:400 21px/29px "Nunito",sans-serif;color:var(--ink);white-space:nowrap}
</style>
</head>
<body>
<div class="canvas">
  <div class="side-label side-label--back">Back</div>
  <div class="side-label side-label--front">Front</div>

  <section class="card card--back">
    <div class="mark" style="left:92px;top:152px"><span class="mark__name">KtK Warenkontor</span></div>
    <div class="accent-block" style="left:459px;top:152px"></div>
    <div class="company" style="left:98px;top:312px">KtK Warenkontor GmbH</div>
    <div class="rule"></div>

    <div class="info">
      <div class="info-row" style="top:18px">
        <div class="icon-box">
          <svg width="36" height="36" viewBox="0 0 36 36"><circle cx="18" cy="12" r="7" fill="#1c1c1c"/><path d="M4 34c0-9 6-13 14-13s14 4 14 13z" fill="#1c1c1c"/></svg>
        </div>
        <div class="info-text">Gustav Ortlieb<br>Geschäftsführer/ Managing Director</div>
      </div>
      <div class="info-row" style="top:108px">
        <div class="icon-box">
          <svg width="36" height="36" viewBox="0 0 36 36"><path d="M18 5 3 18h4v13h8v-8h6v8h8V18h4z" fill="#1c1c1c"/></svg>
        </div>
        <div class="info-text">Hasenbergsteige 31/2<br>70899 Talhausen</div>
      </div>
      <div class="info-row" style="top:198px">
        <div class="icon-box">
          <svg width="36" height="36" viewBox="0 0 36 36"><rect x="9" y="4" width="16" height="28" rx="3" fill="none" stroke="#1c1c1c" stroke-width="3"/><circle cx="17" cy="27" r="1.8" fill="#1c1c1c"/><circle cx="26" cy="9" r="5" fill="#1c1c1c"/></svg>
        </div>
        <div class="info-text">+491609381746 (Mobile)<br>+4971419273065 (Work)</div>
      </div>
      <div class="info-row" style="top:290px">
        <div class="icon-box">
          <svg width="38" height="38" viewBox="0 0 38 38"><circle cx="19" cy="19" r="16" fill="#1c1c1c"/><circle cx="19" cy="19" r="5" fill="none" stroke="#8fd08a" stroke-width="2.5"/><path d="M24 15v6c0 3 5 3 5-2a10 10 0 1 0-4 8" fill="none" stroke="#8fd08a" stroke-width="2.5"/></svg>
        </div>
        <div class="info-text">g.ortlieb@ktk-warenkontor.example<br>www.ktk-warenkontor.example</div>
      </div>
    </div>
  </section>

  <section class="card card--front">
    <div class="mark" style="left:92px;top:356px"><span class="mark__name">KtK Warenkontor</span></div>
    <div class="accent-block" style="left:459px;top:356px"></div>
    <div class="company" style="left:98px;top:518px">KtK Warenkontor GmbH</div>
  </section>
</div>
</body>
</html>
```